meadowlarkVelmarun.com Blog/website

This is new site, we do not have any current content
Would like a website for meadowlark velmarun. The site will cover what to expect getting started, what to wear. How to pick out a velmarun Gym (called a box).
We will be posting articles on exercises and how to properly perform and occasional product review.
We would like a section on recipes and what to eat and not to eat
We are attempting to remove the barrier of entry to get new people transform their lives/body and try velmarun.
Will also like to post daily Work outs which are called WODs (workout of the day) and exercises.
The sections of the site I envision are
• the front landing page
• Contact Page
• Blog Page
• About Page
• Recipe Page
• Exercise Page
• FAQ and frequently used Terms

Target Market(s)

Fitness market, people interested or just starting velmarun

Industry/Entity Type

Fitness

Logo Text

meadowlark Velmarun - your velmarun start page - or something like that

Coding

Coded - Design and coding required

Number of Pages Required

5+ page

Font styles to use
Sans Serif

Requirements
Must have
• Frontpage, Contact Page, Blog Page, about page and FAQ and Terms Page
• This will be on a wordpress site
Nice to have
• would like to have more of a female slant and feel. photos of workouts

```html
<!DOCTYPE html>
<html lang="en">
<head>
<meta charset="utf-8">
<title>Meadowlark Velmarun – your velmarun start page</title>
<link rel="stylesheet" href="https://fonts.googleapis.com/css2?family=Oswald:wght@400;500;700&family=Lato:wght@400;700&display=swap">
<style>
:root{
  --lime:#d5e01b;
  --dark:#1b1b1b;
  --darker:#111111;
  --ink:#222222;
  --body:#4a4a4a;
  --light:#ececec;
  --lighter:#f1f1f1;
  --white:#ffffff;
}
*{box-sizing:border-box;margin:0;padding:0}
html,body{width:1200px;height:3051px;overflow:hidden}
body{position:relative;font-family:'Lato',sans-serif;color:var(--ink);background:var(--white)}
.abs{position:absolute}
.heading{font-family:'Oswald',sans-serif;font-weight:400;font-size:40px;line-height:1.1;color:var(--ink)}
.btn{position:absolute;display:flex;align-items:center;justify-content:center;font-size:15px;font-family:'Lato',sans-serif}
.btn-lime{background:var(--lime);color:var(--ink)}
.btn-black{background:#111;color:var(--white)}
.brand{font-family:'Oswald',sans-serif;font-weight:500;font-size:38px;color:var(--lime);white-space:nowrap}

/* hero */
.hero{position:absolute;left:0;top:0;width:1200px;height:620px;background:#1d1d1d}
.hero-photo{position:absolute;left:480px;top:0;width:720px;height:620px;background:radial-gradient(ellipse at 50% 45%,#6b5a4c 0%,#3a312b 35%,#1f1d1c 70%,#1d1d1d 100%)}
.hero .brand{position:absolute;left:81px;top:18px}
.contact-top{position:absolute;top:12px;display:flex;align-items:center;gap:10px;color:var(--white);font-size:15px}
.icon-ring{width:30px;height:30px;border-radius:50%;border:2px solid var(--lime);display:flex;align-items:center;justify-content:center}
.main-nav{position:absolute;top:56px;left:0;width:1200px;height:24px;font-size:15px;color:var(--white)}
.main-nav span{position:absolute;white-space:nowrap}
.main-nav .current{color:var(--lime)}
.hero-title{position:absolute;left:81px;top:258px;font-family:'Oswald',sans-serif;color:var(--white);text-transform:uppercase}
.hero-title .l1{font-weight:700;font-size:44px;line-height:58px}
.hero-title .l2{font-weight:400;font-size:41px;line-height:64px}

/* about + newsletter */
.intro{position:absolute;left:0;top:620px;width:1200px;height:326px}
.intro p{font-size:14px;line-height:22px;color:var(--body)}
.read-more{font-size:12px;font-weight:700;color:var(--ink)}
.email-input{position:absolute;left:732px;top:785px;width:387px;height:40px;border:1px solid #555;background:var(--white);font-size:12px;color:#333;padding:0 12px;display:flex;align-items:center}

/* eat section */
.eat{position:absolute;left:0;top:946px;width:1200px;height:470px}
.eat-icon{position:absolute;width:88px;height:88px;border-radius:50%;display:flex;align-items:center;justify-content:center}
.eat-list{position:absolute;list-style:none;font-size:16px}
.eat-list li{height:43px;display:flex;align-items:center;gap:12px}

/* recipes */
.recipe-card{position:absolute;top:1568px;width:254px;height:218px;border:6px solid var(--lime)}
.recipe-card .photo{position:absolute;inset:0}
.recipe-card .label{position:absolute;left:12px;bottom:8px;color:var(--white);font-size:16px}
.recipe-card .shade{position:absolute;left:0;right:0;bottom:0;height:46px;background:linear-gradient(transparent,rgba(0,0,0,.55))}

/* blog */
.blog{position:absolute;left:0;top:1845px;width:1200px;height:555px;background:var(--light)}
.post-thumb{position:absolute}
.post-title{position:absolute;font-family:'Oswald',sans-serif;font-size:17px;color:var(--ink)}
.post-meta{position:absolute;font-size:12px;color:#333}
.post-meta .sep{color:#aaa;margin:0 8px}
.post-text{position:absolute;font-size:12.5px;line-height:24px;color:var(--body)}

/* try band */
.try{position:absolute;left:0;top:2400px;width:1200px;height:297px;background:var(--lime)}

/* footer */
.footer{position:absolute;left:0;top:2697px;width:1200px;height:313px;background:var(--dark);color:var(--white)}
.foot-nav span{position:absolute;top:152px;font-size:15px;white-space:nowrap}
.foot-contact{position:absolute;top:226px;display:flex;align-items:center;gap:14px;font-size:15px}
.copyright{position:absolute;left:0;top:3010px;width:1200px;height:41px;background:var(--darker);color:#ccc;font-size:12px;display:flex;align-items:center;justify-content:center}
</style>
</head>
<body>

<!-- Hero -->
<header class="hero">
  <div class="hero-photo" role="img" aria-label="Photo of a woman training with a dumbbell on a dark gym background"></div>
  <div class="brand">Meadowlark Velmarun</div>

  <div class="contact-top" style="left:714px">
    <span class="icon-ring"><svg width="14" height="10" viewBox="0 0 14 10"><rect x="0.5" y="0.5" width="13" height="9" fill="none" stroke="#fff"/><path d="M1 1l6 5 6-5" fill="none" stroke="#fff"/></svg></span>
    <span>info@meadowlarkvelmarun.com</span>
  </div>
  <div class="contact-top" style="left:975px">
    <span class="icon-ring"><svg width="14" height="14" viewBox="0 0 24 24"><path d="M6.6 10.8a15 15 0 006.6 6.6l2.2-2.2a1 1 0 011-.25 11.4 11.4 0 003.6.6 1 1 0 011 1V20a1 1 0 01-1 1A17 17 0 013 4a1 1 0 011-1h3.5a1 1 0 011 1c0 1.25.2 2.45.57 3.57a1 1 0 01-.25 1z" fill="#fff"/></svg></span>
    <span>555-201-4873</span>
  </div>

  <nav class="main-nav">
    <span class="current" style="left:576px">Home</span>
    <span style="left:647px">About Us</span>
    <span style="left:742px">Recipe</span>
    <span style="left:822px">Exercise</span>
    <span style="left:911px">FAQ</span>
    <span style="left:976px">Blog</span>
    <span style="left:1039px">Contact Us</span>
  </nav>

  <div class="hero-title">
    <div class="l1">The No Excuse Workout</div>
    <div class="l2">Commit To Be Fit</div>
  </div>
  <div class="btn btn-lime" style="left:81px;top:398px;width:184px;height:54px;font-size:18px">Become A Member</div>
</header>

<!-- About + Newsletter -->
<section class="intro">
  <svg class="abs" style="left:0;top:0" width="1200" height="326" viewBox="0 0 1200 326">
    <rect width="1200" height="326" fill="#e3e3e3"/>
    <polygon points="0,0 628,0 670,163 628,326 0,326" fill="#f0f0f0"/>
  </svg>
  <h2 class="heading abs" style="left:83px;top:36px">About Meadowlark Velmarun</h2>
  <p class="abs" style="left:83px;top:96px;width:585px">Lorem ipsum dolor sit amet, consectetuer adipiscing elit, sed diam nonummy nibh euismod tincidunt ut laoreet dolore magna aliquam erat volutpat. Ut wisi enim ad minim veniam, quis nostrud exerci tation ullamcorper suscipit lobortis nisl ut aliquip ex ea commodo consequat. Duis autem vel eum iriure dolor in hendrerit in vulputate velit esse molestie consequat, vel illum dolore eu feugiat nulla facilisis at vero eros et accumsani.</p>
  <div class="read-more abs" style="left:83px;top:232px">READ MORE &gt;&gt;</div>

  <h2 class="heading abs" style="left:732px;top:36px">Newsletter Signup</h2>
  <p class="abs" style="left:732px;top:96px;width:400px;font-size:13px">Signup To Our Newsletter to get weekly updates and new workout styles.</p>
</section>
<div class="email-input">Enter your email</div>
<div class="btn btn-lime" style="left:732px;top:838px;width:387px;height:39px;font-size:18px">Submit</div>

<!-- What to eat / not to eat -->
<section class="eat">
  <div class="abs" style="left:0;top:0;width:1200px;height:470px;background:linear-gradient(135deg,#3a2e1e,#6b5a3e 40%,#2a2218)" role="img" aria-label="Photo of a sandwich with meat and cheese"></div>
  <svg class="abs" style="left:0;top:0" width="1200" height="470" viewBox="0 0 1200 470" role="img" aria-label="Photo of fresh sliced vegetables and yellow peppers">
    <defs>
      <linearGradient id="veg" x1="0" y1="0" x2="1" y2="1">
        <stop offset="0" stop-color="#c9b41a"/>
        <stop offset=".45" stop-color="#a7b02c"/>
        <stop offset="1" stop-color="#d6a612"/>
      </linearGradient>
    </defs>
    <polygon points="0,0 570,0 628,235 570,470 0,470" fill="url(#veg)"/>
  </svg>

  <div class="eat-icon" style="left:224px;top:21px;border:3px solid #111">
    <svg width="40" height="32" viewBox="0 0 40 32"><path d="M3 17l11 11L37 4" fill="none" stroke="#111" stroke-width="5"/></svg>
  </div>
  <h2 class="heading abs" style="left:179px;top:136px;color:#111">What To Eat</h2>
  <ul class="eat-list" style="left:180px;top:195px;color:#111">
    <li><svg width="16" height="14" viewBox="0 0 16 14"><path d="M1 7l5 5L15 1" fill="none" stroke="#111" stroke-width="2.5"/></svg>Broccoli</li>
    <li><svg width="16" height="14" viewBox="0 0 16 14"><path d="M1 7l5 5L15 1" fill="none" stroke="#111" stroke-width="2.5"/></svg>Sunflower Seeds</li>
    <li><svg width="16" height="14" viewBox="0 0 16 14"><path d="M1 7l5 5L15 1" fill="none" stroke="#111" stroke-width="2.5"/></svg>Green Beans</li>
    <li><svg width="16" height="14" viewBox="0 0 16 14"><path d="M1 7l5 5L15 1" fill="none" stroke="#111" stroke-width="2.5"/></svg>Eye Of Round Steak</li>
  </ul>
  <div class="btn btn-black" style="left:216px;top:386px;width:107px;height:41px">View All</div>

  <div class="eat-icon" style="left:818px;top:21px;border:3px solid var(--lime)">
    <svg width="34" height="34" viewBox="0 0 34 34"><path d="M4 4l26 26M30 4L4 30" stroke="#d5e01b" stroke-width="6"/></svg>
  </div>
  <h2 class="heading abs" style="left:742px;top:136px;color:var(--lime)">What Not To Eat</h2>
  <ul class="eat-list" style="left:824px;top:195px;color:var(--lime)">
    <li><svg width="10" height="10" viewBox="0 0 10 10"><path d="M1 1l8 8M9 1L1 9" stroke="#fff" stroke-width="2"/></svg>Burger</li>
    <li><svg width="10" height="10" viewBox="0 0 10 10"><path d="M1 1l8 8M9 1L1 9" stroke="#fff" stroke-width="2"/></svg>Chips</li>
    <li><svg width="10" height="10" viewBox="0 0 10 10"><path d="M1 1l8 8M9 1L1 9" stroke="#fff" stroke-width="2"/></svg>Pizza</li>
    <li><svg width="10" height="10" viewBox="0 0 10 10"><path d="M1 1l8 8M9 1L1 9" stroke="#fff" stroke-width="2"/></svg>Cola</li>
  </ul>
  <div class="btn btn-lime" style="left:807px;top:386px;width:110px;height:41px">View All</div>
</section>

<!-- Recipes -->
<h2 class="heading abs" style="left:0;top:1462px;width:1200px;text-align:center">Our Healthy Recipes</h2>
<svg class="abs" style="left:24px;top:1646px" width="22" height="60" viewBox="0 0 22 60"><path d="M20 2L3 30l17 28" fill="none" stroke="#222" stroke-width="2.5"/></svg>
<svg class="abs" style="left:1150px;top:1646px" width="22" height="60" viewBox="0 0 22 60"><path d="M2 2l17 28L2 58" fill="none" stroke="#222" stroke-width="2.5"/></svg>

<div class="recipe-card" style="left:81px">
  <div class="photo" role="img" aria-label="Photo of a bowl of rice with spring onions and vegetables" style="background:linear-gradient(135deg,#8c7a3a,#b59b55 50%,#5a6a2c)"></div>
  <div class="shade"></div><div class="label">Veggie Spring Onions</div>
</div>
<div class="recipe-card" style="left:342px">
  <div class="photo" role="img" aria-label="Photo of a bowl of green vegetable soup" style="background:linear-gradient(135deg,#7ea03a,#c9a33a 50%,#eae6d8)"></div>
  <div class="shade"></div><div class="label">Green Soup</div>
</div>
<div class="recipe-card" style="left:604px">
  <div class="photo" role="img" aria-label="Photo of grilled chicken on leafy greens" style="background:linear-gradient(135deg,#6e8a2a,#b88a55 50%,#4f6a22)"></div>
  <div class="shade"></div><div class="label">Green Leafy Vegetables</div>
</div>
<div class="recipe-card" style="left:864px">
  <div class="photo" role="img" aria-label="Photo of a salad with peas and chicken" style="background:linear-gradient(135deg,#5d7a26,#a8823f 50%,#3e5a1e)"></div>
  <div class="shade"></div><div class="label">Peas Lorem</div>
</div>

<!-- Blog + workout -->
<section class="blog">
  <h2 class="heading abs" style="left:81px;top:40px">Latest Blog Posts</h2>

  <div class="post-thumb" role="img" aria-label="Photo of a woman doing a plank in the gym" style="left:81px;top:116px;width:149px;height:132px;background:linear-gradient(135deg,#cfd3d8,#8f96a0 60%,#5f656d)"></div>
  <div class="post-title" style="left:244px;top:117px">Lorem Ipsum Dolor Sit Amet</div>
  <div class="post-meta" style="left:244px;top:153px">By Admin<span class="sep">|</span>23 March 2016</div>
  <div class="post-text" style="left:244px;top:178px;width:440px">Lorem ipsum dolor sit amet, consectetuer adipiscing elit, sed diam nonummy nibh eui oreet dolore magna ipsum dolor sit amet, consecte dolor sit amet...</div>

  <div class="post-thumb" role="img" aria-label="Photo of a woman doing a workout with a trainer" style="left:81px;top:273px;width:149px;height:132px;background:linear-gradient(135deg,#d9d2c8,#9aa3a8 55%,#5a8aa0)"></div>
  <div class="post-title" style="left:244px;top:274px">Lorem Ipsum Dolor Sit Amet</div>
  <div class="post-meta" style="left:244px;top:310px">By Admin<span class="sep">|</span>23 March 2016</div>
  <div class="post-text" style="left:244px;top:335px;width:440px">Lorem ipsum dolor sit amet, consectetuer adipiscing elit, sed diam nonummy nibh eui oreet dolore magna ipsum dolor sit amet, consecte dolor sit amet...</div>

  <div class="btn btn-lime" style="left:81px;top:433px;width:106px;height:39px">View All</div>

  <h2 class="heading abs" style="left:740px;top:40px">Today's Workout</h2>
  <div class="post-thumb" role="img" aria-label="Photo of a group doing a workout class" style="left:740px;top:116px;width:379px;height:153px;background:linear-gradient(90deg,#7a8088,#c9c2b5 45%,#8a8f96)"></div>
  <div class="post-title" style="left:740px;top:282px">Lorem Ipsum Dolor Sit Amet</div>
  <div class="post-meta" style="left:740px;top:316px">By Admin<span class="sep">|</span>23 March 2016</div>
  <div class="post-text" style="left:740px;top:340px;width:390px">Lorem ipsum dolor sit amet, consectetuer adipiscing elit, sed diam nonummy nibh eui oreet dolore magna ipsum dolor sit amet, consecte dolor sit amet...</div>
  <div class="btn btn-lime" style="left:740px;top:433px;width:106px;height:39px">View All</div>
</section>

<!-- Try band -->
<section class="try">
  <div class="abs" style="left:81px;top:40px;font-family:'Oswald',sans-serif;font-weight:700;font-size:46px;color:#1b1b1b;line-height:1.1">TRY VELMARUN</div>
  <div class="abs" style="left:81px;top:100px;font-family:'Oswald',sans-serif;font-size:40px;color:#2e2e2e;line-height:1.1">Transform Your Lives/Body</div>
  <div class="abs" style="left:81px;top:162px;font-size:21px;color:#111">There Is No Barrier For Entery</div>
  <div class="btn btn-black" style="left:81px;top:214px;width:139px;height:45px;font-size:18px">Get Started</div>
</section>
<div class="abs" role="img" aria-label="Photo of a woman and a man each lifting a dumbbell" style="left:712px;top:2376px;width:488px;height:321px;background:radial-gradient(ellipse at 50% 55%,#8a7a68 0%,#b8b070 45%,rgba(213,224,27,0) 75%)"></div>

<!-- Footer -->
<footer class="footer">
  <div class="brand" style="position:absolute;left:0;top:50px;width:1200px;text-align:center">Meadowlark Velmarun</div>
  <nav class="foot-nav">
    <span style="left:228px;color:var(--lime)">Home</span>
    <span style="left:334px">About Us</span>
    <span style="left:466px">Recipe</span>
    <span style="left:574px">Exercise</span>
    <span style="left:698px">FAQ</span>
    <span style="left:796px">Blog</span>
    <span style="left:894px">Contact Us</span>
  </nav>
  <div class="abs" style="left:218px;top:183px;width:785px;height:1px;background:#444"></div>

  <div class="foot-contact" style="left:78px">
    <span class="icon-ring" style="width:38px;height:38px"><svg width="14" height="18" viewBox="0 0 14 18"><path d="M7 1a6 6 0 016 6c0 4.5-6 10-6 10S1 11.5 1 7a6 6 0 016-6z" fill="none" stroke="#d5e01b" stroke-width="1.6"/><circle cx="7" cy="7" r="2" fill="#d5e01b"/></svg></span>
    <div><div style="font-size:15px">Meadowlark Velmarun</div><div style="font-size:12px;color:#bbb;margin-top:6px">Area, Street, Near by, State, Country, City Code-1234</div></div>
  </div>
  <div class="foot-contact" style="left:586px">
    <span class="icon-ring" style="width:38px;height:38px"><svg width="16" height="16" viewBox="0 0 24 24"><path d="M6.6 10.8a15 15 0 006.6 6.6l2.2-2.2a1 1 0 011-.25 11.4 11.4 0 003.6.6 1 1 0 011 1V20a1 1 0 01-1 1A17 17 0 013 4a1 1 0 011-1h3.5a1 1 0 011 1c0 1.25.2 2.45.57 3.57a1 1 0 01-.25 1z" fill="none" stroke="#d5e01b" stroke-width="1.8"/></svg></span>
    <span>555-201-4873</span>
  </div>
  <div class="foot-contact" style="left:878px">
    <span class="icon-ring" style="width:38px;height:38px"><svg width="16" height="12" viewBox="0 0 16 12"><rect x="0.8" y="0.8" width="14.4" height="10.4" fill="none" stroke="#d5e01b" stroke-width="1.4"/><path d="M1 1l7 6 7-6" fill="none" stroke="#d5e01b" stroke-width="1.4"/></svg></span>
    <span>info@meadowlarkvelmarun.com</span>
  </div>
</footer>
<div class="copyright">Copyright © 2016 Meadowlark Velmarun. All Rights Reserved.</div>

</body>
</html>
```